Clean and modern business cards

Looking for an updated business card design for my dental office “corvanta dental” . Looking for a modern clean / sleek design . I’m thinking black background but open to seeing other options . One side needs to have an appointment card . Card needs to have logo, dentist name , phone, email , address . I’ve attached couple of cards I thought were cool as well as my logo
Target Market(s)
Dental patients
Industry/Entity Type
Dentistry
Contact Information for Business Card
Phone email address

```html
<!DOCTYPE html>
<html lang="en">
<head>
<meta charset="utf-8">
<title>Corvanta Dental — Business Card</title>
<link rel="stylesheet" href="https://fonts.googleapis.com/css2?family=Montserrat:wght@400;600;700&family=Roboto+Condensed:wght@400&family=Roboto:wght@400&display=swap">
<style>
  :root {
    --page-bg: #2f2f30;
    --card-bg: #262627;
    --card-bg-light: #303031;
    --text-white: #f2f2f2;
    --text-soft: #dcdcdc;
    --accent-yellow: #e2b415;
    --accent-green: #9bb525;
    --accent-blue: #1a8cc7;
    --accent-magenta: #93226f;
    --accent-grey: #a4a4a4;
    --field-bg: #ececec;
    --ink: #1d1d1d;
  }
  * { margin: 0; padding: 0; box-sizing: border-box; }
  html, body { width: 1200px; height: 1138px; overflow: hidden; }
  body {
    background: var(--page-bg);
    font-family: "Montserrat", sans-serif;
    position: relative;
  }
  .card {
    position: absolute;
    width: 622px;
    height: 375px;
    border-radius: 16px;
    background: linear-gradient(135deg, var(--card-bg-light), var(--card-bg));
    overflow: hidden;
    color: var(--text-white);
  }
  .card--appointment { left: 275px; top: 186px; }
  .card--contact { left: 277px; top: 608px; }

  /* wordmark */
  .wordmark { position: absolute; color: var(--text-white); font-weight: 700; line-height: 1; }
  .wordmark__name { display: block; letter-spacing: 0.5px; }
  .wordmark__sub { display: block; letter-spacing: 6px; text-align: right; }
  .card--appointment .wordmark { left: 28px; top: 102px; }
  .card--appointment .wordmark__name { font-size: 44px; }
  .card--appointment .wordmark__sub { font-size: 19px; margin-top: 6px; font-weight: 700; }
  .card--contact .wordmark { left: 378px; top: 282px; width: 220px; text-align: center; }
  .card--contact .wordmark__name { font-size: 34px; }
  .card--contact .wordmark__sub { font-size: 15px; margin-top: 4px; text-align: center; }

  .decor-area {
    position: absolute;
    left: 290px; top: 0;
    width: 332px; height: 276px;
    background: radial-gradient(circle at 55% 45%, #4a4a4b 0%, #333334 45%, rgba(38,38,39,0) 75%);
  }

  .appointment__label {
    position: absolute; left: 23px; top: 260px;
    font-size: 17px; font-weight: 400; color: var(--text-soft);
  }
  .appointment__field {
    position: absolute; left: 23px; top: 289px;
    width: 576px; height: 43px;
    background: linear-gradient(90deg, var(--field-bg), #ffffff 50%, var(--field-bg));
    display: flex; align-items: center; gap: 6px;
    padding: 6px 12px 0;
    font-family: "Roboto", sans-serif; font-size: 17px; color: var(--ink);
  }
  .appointment__line { flex: 1; border-bottom: 1.5px solid var(--ink); height: 14px; }
  .appointment__line--date { flex: 1.15; margin-right: 6px; }
  .appointment__notice {
    position: absolute; left: 23px; top: 338px;
    font-family: "Roboto Condensed", sans-serif; font-size: 14.5px; color: var(--text-soft);
    white-space: nowrap;
  }

  .dentist__name {
    position: absolute; left: 29px; top: 50px;
    font-size: 24px; font-weight: 700; color: var(--accent-yellow);
  }
  .dentist__credentials {
    position: absolute; left: 29px; top: 79px;
    font-size: 17px; color: var(--text-soft);
  }
  .contact__address {
    position: absolute; left: 29px; top: 211px;
    font-size: 17px; line-height: 24px; color: var(--text-soft); font-style: normal;
  }
  .contact__list {
    position: absolute; left: 29px; top: 263px;
    list-style: none; font-size: 17px; color: var(--text-soft);
  }
  .contact__item { display: flex; align-items: center; height: 24px; }
  .contact__icon { width: 16px; height: 16px; margin-right: 16px; }

  .color-band {
    position: absolute; left: 0; bottom: 0; width: 100%; height: 11px; display: flex;
  }
  .color-band span { flex: 1; }
  .color-band .blue { background: var(--accent-blue); }
  .color-band .yellow { background: var(--accent-yellow); }
  .color-band .green { background: var(--accent-green); }
  .color-band .magenta { background: var(--accent-magenta); }
  .color-band .grey { background: var(--accent-grey); }
</style>
</head>
<body>

<section class="card card--appointment">
  <div class="wordmark">
    <span class="wordmark__name">CORVANTA</span>
    <span class="wordmark__sub">DENTAL</span>
  </div>
  <div class="decor-area" role="img" aria-label="Embossed decorative pattern of circles around a tooth mark"></div>
  <p class="appointment__label">Your Next Appointment is:</p>
  <div class="appointment__field">
    <span>Date:</span><span class="appointment__line appointment__line--date"></span>
    <span>Time:</span><span class="appointment__line"></span>
  </div>
  <p class="appointment__notice">To cancel/reschedule please notify us at least 48 hours prior to your scheduled appointment</p>
</section>

<section class="card card--contact">
  <h1 class="dentist__name">DR TEODOR</h1>
  <p class="dentist__credentials">Bsc (dent) DMD</p>
  <address class="contact__address">214–880 Larchmont Ave<br>Winnipeg, MB R3K 2T7</address>
  <ul class="contact__list">
    <li class="contact__item">
      <svg class="contact__icon" viewBox="0 0 16 16" aria-hidden="true"><path fill="#e2b415" d="M2 5c0-2 2-3 6-3s6 1 6 3v1h-3V5H5v1H2zM4 7h8l2 6H2zM8 8.5a2 2 0 1 0 0 4 2 2 0 0 0 0-4z"/></svg>
      <span>204-555-0142</span>
    </li>
    <li class="contact__item">
      <svg class="contact__icon" viewBox="0 0 16 16" aria-hidden="true"><rect x="1" y="3" width="14" height="10" fill="#9bb525"/><path d="M1 3l7 6 7-6M1 13l5-5M15 13l-5-5" stroke="#262627" stroke-width="1.2" fill="none"/></svg>
      <span>contact@corvantawpg.ca</span>
    </li>
    <li class="contact__item">
      <svg class="contact__icon" viewBox="0 0 16 16" aria-hidden="true"><g fill="none" stroke="#93226f" stroke-width="1.4"><circle cx="8" cy="8" r="6.5"/><ellipse cx="8" cy="8" rx="3" ry="6.5"/><path d="M1.5 8h13M2.5 5h11M2.5 11h11"/></g></svg>
      <span>www.corvantawpg.ca</span>
    </li>
  </ul>
  <div class="wordmark">
    <span class="wordmark__name">CORVANTA</span>
    <span class="wordmark__sub">DENTAL</span>
  </div>
  <div class="color-band">
    <span class="blue"></span><span class="yellow"></span><span class="green"></span><span class="magenta"></span><span class="grey"></span>
  </div>
</section>

</body>
</html>
```